Postcard Design

Landscaping Company
Lawn Cuts
Mulch
Spring Clean Ups
Planting

Company Name - RVM GROUNDWORK PARTNERS
ADDRESS - 47 Kestwick Rd.
N. Hanover, NJ 08599
Phone #- 609-555-0148

Target Market(s)

Direct mailer looking to draw in new clients

Industry/Entity Type

It Company

Requirements
Must have
• Eye catching

```html
<!DOCTYPE html>
<html lang="en">
<head>
<meta charset="utf-8">
<title>RVM Groundwork Partners – Postcard</title>
<link rel="stylesheet" href="https://fonts.googleapis.com/css2?family=Montserrat:wght@300;400;600;700;800&display=swap">
<style>
  :root {
    --brand-green: #0f9444;
    --grass-dark: #1f5e2a;
    --grass-mid: #4f9a3a;
    --body-top: #d3dbc9;
    --body-bottom: #eff1ec;
    --ink: #111111;
    --white: #ffffff;
  }
  * { margin: 0; padding: 0; box-sizing: border-box; }
  html, body { width: 924px; height: 1200px; overflow: hidden; background: var(--white); }
  .postcard {
    position: relative;
    width: 924px;
    height: 1200px;
    font-family: "Montserrat", Arial, sans-serif;
    background: linear-gradient(180deg, var(--body-top) 0%, var(--body-bottom) 70%, var(--white) 100%);
    overflow: hidden;
  }
  .masthead {
    position: absolute; left: 0; top: 0; width: 100%; height: 322px;
    background: var(--brand-green);
    color: var(--white);
    text-align: center;
    padding-top: 58px;
  }
  .company-name {
    font-weight: 700;
    line-height: 0.95;
  }
  .company-name .line-1 { display: block; font-size: 74px; letter-spacing: -1px; }
  .company-name .line-2 { display: block; font-size: 64px; margin-top: 4px; }
  .address {
    margin-top: 22px;
    font-size: 34px;
    font-weight: 600;
  }
  .services {
    position: absolute; left: 77px; top: 420px;
    color: var(--ink);
  }
  .services-heading {
    font-size: 45px; font-weight: 700; letter-spacing: -1.5px;
    margin-bottom: 26px;
  }
  .service-list { list-style: none; margin-left: 39px; }
  .service-list li {
    display: flex; align-items: center;
    font-size: 47px; font-weight: 300;
    height: 65px;
  }
  .service-list svg { width: 20px; height: 26px; margin-right: 26px; flex: none; }
  .slogan-box {
    position: absolute; left: 614px; top: 339px; width: 271px; height: 570px;
    background: var(--brand-green);
    color: var(--white);
    padding: 88px 0 0 21px;
    font-weight: 700;
    line-height: 0.98;
    text-transform: uppercase;
  }
  .slogan-box span { display: block; }
  .slogan-box .s-a { font-size: 52px; }
  .slogan-box .s-happy { font-size: 56px; }
  .slogan-box .s-home { font-size: 62px; letter-spacing: -1px; }
  .slogan-box .s-needs { font-size: 48px; }
  .slogan-box .s-yards { font-size: 58px; }
  .grass-art {
    position: absolute; left: 0; top: 862px; width: 100%; height: 220px;
    background: linear-gradient(180deg, rgba(79,154,58,0) 0%, var(--grass-mid) 45%, var(--grass-dark) 100%);
  }
  .call-bar {
    position: absolute; left: 0; top: 1082px; width: 100%; height: 118px;
    background: var(--brand-green);
    color: var(--white);
    display: flex; align-items: center; justify-content: center;
    font-size: 42px; font-weight: 700;
  }
  .call-bar .divider {
    width: 4px; height: 84px; background: var(--white);
    margin: 0 22px;
  }
  .call-bar .phone { font-weight: 600; }
</style>
</head>
<body>
  <div class="postcard">
    <header class="masthead">
      <h1 class="company-name">
        <span class="line-1">RVM GROUNDWORK</span>
        <span class="line-2">PARTNERS</span>
      </h1>
      <p class="address">47 Kestwick Rd. N. Hanover, NJ 08599</p>
    </header>

    <section class="services">
      <h2 class="services-heading">WHAT DO WE DO?</h2>
      <ul class="service-list">
        <li><svg viewBox="0 0 20 26"><polyline points="3,2 16,13 3,24" fill="none" stroke="#111" stroke-width="3"/></svg>Landscape</li>
        <li><svg viewBox="0 0 20 26"><polyline points="3,2 16,13 3,24" fill="none" stroke="#111" stroke-width="3"/></svg>Lawn Cuts</li>
        <li><svg viewBox="0 0 20 26"><polyline points="3,2 16,13 3,24" fill="none" stroke="#111" stroke-width="3"/></svg>Mulch</li>
        <li><svg viewBox="0 0 20 26"><polyline points="3,2 16,13 3,24" fill="none" stroke="#111" stroke-width="3"/></svg>Spring Clean Ups</li>
        <li><svg viewBox="0 0 20 26"><polyline points="3,2 16,13 3,24" fill="none" stroke="#111" stroke-width="3"/></svg>Planting</li>
      </ul>
    </section>

    <aside class="slogan-box">
      <span class="s-a">A</span>
      <span class="s-happy">Happy</span>
      <span class="s-home">Home</span>
      <span class="s-needs">Needs</span>
      <span class="s-a">A</span>
      <span class="s-happy">Happy</span>
      <span class="s-yards">Yards</span>
    </aside>

    <div class="grass-art" role="img" aria-label="Illustration of a row of green grass blades and leaves along the bottom"></div>

    <footer class="call-bar">
      <span class="cta">CALL NOW!</span>
      <span class="divider"></span>
      <span class="phone">609-555-0148</span>
    </footer>
  </div>
</body>
</html>
```